Web site for Life Coaching Consultant

I require a website for a life coaching business. I have a Tidal Netware account which I set up last week. I will need to be able to add articles and testimonials. The design should communicate that RL Harbor Lanterns is there to help people breakdown personal barriers and that we are an advocate to help them achieve personal goals.
Updates

Reason: I have some designers just accepting my invitation to submit so to give them a few days to submit. I have been thrilled with the quality of the submissions Thank you.

Hi everyone

I am loving all your designs.  The only feedback I can get from people is that they feel that the runner makes the web page look like a personal coach rather than a life coach that helps people with relations, career, and personal road blocks.

Sorry                                   

Reason: Hi I have increased the deadline as there has been so many amazing designs and some of you have asked to fine tune your entries. I would like to take this opportunity to thank you all. It is going to be a tough decision. I have put a few more pictures on the project page hoping this will help

Hi I just wanted to thank you all for your great designs.  As I got so many good designs I have asked people to vote.  I will be in touch in the next day or 2.

Cheers

Target Market(s)

People with self esteem issues either woman or girls, people who want to goal set and need an advocate

Industry/Entity Type

Life Coaching

Colors
d2a4cc
e567a6

Requirements
Must have
• must have bio section, logo, articles page, affirmation section and testimonial page.

```html
<!DOCTYPE html>
<html lang="en">
<head>
<meta charset="utf-8">
<title>Harbor Lanterns – Life Coaching</title>
<link rel="stylesheet" href="https://fonts.googleapis.com/css2?family=Source+Sans+3:ital,wght@0,400;0,600;0,700;1,400&family=Delius&display=swap">
<style>
  :root {
    --pink: #e5197a;
    --pink-soft: #fdeef6;
    --pink-logo: rgba(210, 120, 170, 0.55);
    --ink: #222222;
    --muted: #777777;
    --body: #444444;
    --white: #ffffff;
    --sidebar: rgba(0, 0, 0, 0.82);
    --panel-dark: #3a3a3a;
    --panel-darker: #262626;
    --rule: #555555;
    --dots: #cccccc;
  }
  * { box-sizing: border-box; margin: 0; padding: 0; }
  html, body { width: 986px; height: 1200px; overflow: hidden; }
  body {
    position: relative;
    font-family: "Source Sans 3", "Open Sans", sans-serif;
    font-size: 12px;
    color: var(--body);
  }
  .backdrop {
    position: absolute; inset: 0;
    background: radial-gradient(ellipse at 75% 85%, #8a8a86 0%, #4b4d49 35%, #2f322f 70%, #1f221f 100%);
  }
  .sidebar {
    position: absolute; left: 0; top: 0; width: 258px; height: 1200px;
    background: var(--sidebar);
  }
  .logo {
    position: absolute; left: 110px; top: 75px; width: 148px; height: 115px;
    background: var(--pink-logo);
    display: flex; flex-direction: column; align-items: center; justify-content: center; gap: 8px;
  }
  .logo-mark { width: 40px; height: 40px; border-radius: 50%; border: 3px solid var(--pink); }
  .logo-name { font-family: "Delius", cursive; font-size: 17px; color: var(--pink); }
  .side-rule { position: absolute; left: 98px; width: 135px; height: 2px; background: var(--rule); }
  .nav { position: absolute; left: 98px; top: 253px; list-style: none; }
  .nav li {
    width: 90px; height: 28px; line-height: 28px; padding-left: 9px; margin-bottom: -2px;
    font-family: "Delius", cursive; font-size: 14px; color: var(--pink);
  }
  .nav li.active { background: var(--pink); color: var(--white); border-radius: 2px; font-weight: 700; }
  .social { position: absolute; left: 100px; top: 465px; display: flex; gap: 7px; }
  .social span { width: 18px; height: 18px; border-radius: 50%; background: var(--white); }
  .about-us { position: absolute; left: 98px; top: 533px; width: 138px; color: var(--white); font-size: 10.5px; line-height: 13.5px; }
  .about-us h3 { font-size: 13px; font-weight: 600; margin-bottom: 14px; }
  .about-us p + p { margin-top: 13px; }
  .subscribe { position: absolute; left: 98px; top: 780px; width: 135px; }
  .subscribe h3 { color: var(--pink); font-size: 12.5px; font-weight: 600; margin-bottom: 14px; }
  .subscribe .field { height: 17px; border: 1px solid #666; background: #222; margin-bottom: 8px; }
  .subscribe .btn { display: inline-block; margin-top: 3px; padding: 0 8px; height: 23px; line-height: 23px; background: var(--pink); color: var(--white); font-size: 11px; }
  .legal { position: absolute; left: 98px; top: 937px; color: var(--white); font-size: 10.5px; line-height: 14px; }

  .search { position: absolute; left: 724px; top: 27px; width: 163px; height: 21px; background: linear-gradient(#fff, #ddd); border-radius: 4px; }
  .search span { position: absolute; left: 12px; top: 4px; font-size: 10px; font-style: italic; color: #555; }
  .search .go { position: absolute; right: 1px; top: 1px; width: 41px; height: 19px; background: #a01552; border-radius: 3px; }

  .hero { position: absolute; left: 258px; top: 75px; width: 629px; height: 277px; background: var(--pink); }
  .hero-photo { position: absolute; left: 0; top: 18px; width: 409px; height: 227px; background: linear-gradient(#9fb3c8, #e7e5dd 60%, #8d8a86); }
  .dots { position: absolute; left: 14px; top: 257px; display: flex; gap: 5px; }
  .dots span { width: 10px; height: 10px; border-radius: 50%; background: var(--dots); }
  .dots span.on { background: #888; border: 2px solid var(--dots); }
  .welcome { position: absolute; left: 381px; top: 7px; width: 234px; height: 258px; background: var(--pink-soft); padding: 21px 25px 0 42px; font-size: 10.5px; line-height: 12.5px; }
  .welcome h2 { color: var(--pink); font-size: 11px; font-weight: 600; margin-bottom: 12px; }
  .welcome p + p { margin-top: 24px; }

  .articles { position: absolute; left: 258px; top: 352px; width: 411px; height: 762px; background: var(--white); }
  .articles-head { height: 40px; border-bottom: 1px solid #e3e3e3; padding: 14px 0 0 22px; font-family: "Delius", cursive; font-size: 13px; color: var(--ink); }
  .article { position: absolute; left: 23px; width: 370px; height: 156px; }
  .article + .article { }
  .article .thumb { position: absolute; left: 0; top: 0; width: 98px; height: 98px; border-radius: 6px; background: linear-gradient(#b8c7a4, #7b8e80 50%, #5a5f58); }
  .article .text { position: absolute; left: 117px; top: -8px; width: 255px; }
  .article h3 { font-size: 17.5px; font-weight: 400; color: var(--pink); }
  .article .date { font-style: italic; color: var(--muted); font-size: 11.5px; margin-top: -3px; }
  .article p { margin-top: 6px; font-size: 10.5px; line-height: 14.6px; }
  .article .more { color: #c8102e; }
  .article .divider { position: absolute; left: 0; top: 126px; width: 368px; border-top: 1px dotted #bbb; }
  .view-all { position: absolute; left: 139px; top: 667px; width: 92px; height: 23px; border: 1px solid var(--pink); color: var(--pink); font-size: 10.5px; line-height: 21px; text-align: center; }

  .testimonials { position: absolute; left: 669px; top: 352px; width: 218px; height: 360px; background: var(--panel-dark); padding: 13px 17px 0 16px; color: var(--white); font-size: 10px; line-height: 12.3px; }
  .testimonials h2 { color: var(--pink); font-size: 11px; font-weight: 600; padding-bottom: 6px; border-bottom: 1px solid var(--pink); margin-bottom: 14px; }
  .quote { height: 156px; }
  .quote + .quote { border-top: 1px solid var(--pink); padding-top: 18px; }
  .quote .avatar { float: left; width: 61px; height: 60px; margin: 0 9px 2px 0; background: linear-gradient(#7c8a98, #4e5a66); border: 2px solid #999; }
  .quote .by { margin-top: 11px; }
  .quote .by b { color: var(--pink); font-weight: 400; }
  .carousel-nav { position: absolute; left: 669px; top: 712px; width: 218px; height: 35px; background: var(--panel-darker); }
  .carousel-nav svg { position: absolute; top: 13px; }
</style>
</head>
<body>
  <div class="backdrop" role="img" aria-label="Background photograph of stepping stones in a stream"></div>

  <aside class="sidebar">
    <div class="logo">
      <span class="logo-mark"></span>
      <span class="logo-name">Harbor Lanterns</span>
    </div>
    <div class="side-rule" style="top:229px"></div>
    <ul class="nav">
      <li class="active">Home</li>
      <li>About</li>
      <li>Articles</li>
      <li>Affirmation</li>
      <li>Testimonials</li>
      <li>Contact</li>
    </ul>
    <div class="side-rule" style="top:443px"></div>
    <div class="social" aria-label="Social links"><span></span><span></span><span></span></div>
    <div class="side-rule" style="top:509px"></div>
    <section class="about-us">
      <h3>About Us</h3>
      <p>Lorem ipsum dolor sit amet, consectetuer adipiscing elit, sed diam nonummy nibh euismod tincidunt ut laoreet dolore magna aliquam erat volutpat. Ut wisi enim ad minim veniam, ullamcorper suscipit lobortis nisl ut aliquip ex ea commodo consequat.</p>
      <p>Dolore magna aliquam erat volutpat. Ut wisi enim ad minim veniam, quis nostrud exerci.</p>
    </section>
    <div class="side-rule" style="top:764px"></div>
    <section class="subscribe">
      <h3>Subscribe to Newsletters</h3>
      <div class="field"></div>
      <div class="field"></div>
      <span class="btn">Subscribe</span>
    </section>
    <div class="side-rule" style="top:911px"></div>
    <p class="legal">Terms and conditions<br>© 2014, Harbor Lanterns.<br>All rights reserved.</p>
  </aside>

  <div class="search">
    <span>Search..</span>
    <div class="go">
      <svg width="41" height="19" viewBox="0 0 41 19"><circle cx="19.5" cy="8.5" r="4" fill="none" stroke="#fff" stroke-width="1.6"/><line x1="22.5" y1="11.5" x2="25.5" y2="14.5" stroke="#fff" stroke-width="1.8"/></svg>
    </div>
  </div>

  <section class="hero">
    <div class="hero-photo" role="img" aria-label="Slide photograph of a woman standing confidently against the sky with a motivational message"></div>
    <div class="dots"><span></span><span class="on"></span><span></span><span></span></div>
    <div class="welcome">
      <h2>WELCOME TO HARBOR LANTERNS</h2>
      <p>Lorem ipsum dolor sit amet sectetuer adipiscing elit, sed diam nonummy ibh euismod tincidunt ut laoreet dolore gna aliquam erat volutpat. Ut wisi enim ad minim veniam, quis nostrud exerci tation.</p>
      <p>Ullamcorper suscipit lobortis nisl ut uip ex ea commodo consequat. Duis autem vel eum iriure dolor in hendrerit in vopu tate velit esse molestie consequat, velil lum dolore eu feugiat nulla facilisis at vero eril delenit augue duis dolore te feugait nulla facilisi.</p>
    </div>
  </section>

  <main class="articles">
    <h2 class="articles-head">Latest Articles</h2>

    <article class="article" style="top:69px">
      <div class="thumb" role="img" aria-label="Photo of stepping stones across a river"></div>
      <div class="text">
        <h3>First headline</h3>
        <div class="date">Posted on Mon 10th Feb 2014</div>
        <p>Sit amet, consectetuer adipiscing elit, sed diam nonum my nibh euismod tincidunt ut laoreet dolore magna aliquam erat volutpat. Ut wisi enim ad minim veniam, ullamcorper suscipcidunt ut laoreet dol it lobortis niscommodo consequat... <span class="more">READ MORE</span></p>
      </div>
      <div class="divider"></div>
    </article>

    <article class="article" style="top:225px">
      <div class="thumb" role="img" aria-label="Photo of stepping stones across a river"></div>
      <div class="text">
        <h3>Second headline is longer</h3>
        <div class="date">Posted on Mon 10th Feb 2014</div>
        <p>Sit amet, consectetuer adipiscing elit, sed diam nonum my nibh euismod tincidunt ut laoreet dolore magna aliquam erat volutpat. Ut wisi enim ad minim veniam, ullamcorper suscipcidunt ut laoreet dol it lobortis niscommodo consequat... <span class="more">READ MORE</span></p>
      </div>
      <div class="divider"></div>
    </article>

    <article class="article" style="top:381px">
      <div class="thumb" role="img" aria-label="Photo of stepping stones across a river"></div>
      <div class="text">
        <h3>Third headline is also longer</h3>
        <div class="date">Posted on Mon 10th Feb 2014</div>
        <p>Sit amet, consectetuer adipiscing elit, sed diam nonum my nibh euismod tincidunt ut laoreet dolore magna aliquam erat volutpat. Ut wisi enim ad minim veniam, ullamcorper suscipcidunt ut laoreet dol it lobortis niscommodo consequat... <span class="more">READ MORE</span></p>
      </div>
      <div class="divider"></div>
    </article>

    <article class="article" style="top:537px">
      <div class="thumb" role="img" aria-label="Photo of stepping stones across a river"></div>
      <div class="text">
        <h3>Forth headline</h3>
        <div class="date">Posted on Mon 10th Feb 2014</div>
        <p>Sit amet, consectetuer adipiscing elit, sed diam nonum my nibh euismod tincidunt ut laoreet dolore magna aliquam erat volutpat. Ut wisi enim ad minim veniam, ullamcorper suscipcidunt ut laoreet dol it lobortis niscommodo consequat... <span class="more">READ MORE</span></p>
      </div>
    </article>

    <a class="view-all">View All Posts &nbsp;›</a>
  </main>

  <section class="testimonials">
    <h2>Testimonials</h2>
    <div class="quote">
      <div class="avatar" role="img" aria-label="Client portrait"></div>
      <p>Lorem ipsum dolor sit amet, consectetuer adipi-scing elit, sed diam non-ummy nibh euismod tincidunt ut laoreet dolore magna aliquam erat volutpat. Ut wisi enim ad minim veniam, quis nostrud exerci tation.</p>
      <p class="by"><b>Dana Whitfield,</b> Lorem ipsum dolor.</p>
    </div>
    <div class="quote">
      <div class="avatar" role="img" aria-label="Client group portrait"></div>
      <p>Lorem ipsum dolor sit amet, consectetuer adipi-scing elit, sed diam non-ummy nibh euismod tincidunt ut laoreet dolore magna aliquam erat volutpat. Ut wisi enim ad minim veniam, quis nostrud exerci tation.</p>
      <p class="by"><b>Dana Whitfield,</b> Lorem ipsum dolor.</p>
    </div>
  </section>
  <nav class="carousel-nav" aria-label="Testimonial navigation">
    <svg style="left:59px" width="12" height="8" viewBox="0 0 12 8"><polyline points="1,7 6,2 11,7" fill="none" stroke="#fff" stroke-width="2"/></svg>
    <svg style="left:146px" width="12" height="8" viewBox="0 0 12 8"><polyline points="1,1 6,6 11,1" fill="none" stroke="#fff" stroke-width="2"/></svg>
  </nav>
</body>
</html>
```